DWR Logistics Marketing flyer

Good morning, I run a trucking company and I will be needing help setting up a website logo and a marketing flyer or something like that talking about our services and what we can offer to potential new customers who need to ship their product. I need help getting this all together.

Target Market(s)

Transportation customers

Requirements
Must have
• should list our services and contact info
Nice to have
• the Logo on the top

```html
<!DOCTYPE html>
<html lang="en">
<head>
<meta charset="utf-8">
<title>DWR Logistics – Marketing Flyer</title>
<link href="https://fonts.googleapis.com/css2?family=Montserrat:wght@600;800&family=Roboto:wght@400;700&family=Roboto+Condensed:wght@700&display=swap" rel="stylesheet">
<style>
  :root{
    --brand-blue:#123f8a;
    --brand-orange:#f29e0c;
    --ink:#1c1c1c;
    --paper:#ffffff;
    --backdrop:#e4e4e4;
  }
  *{margin:0;padding:0;box-sizing:border-box}
  html,body{width:1200px;height:2804px;overflow:hidden;background:var(--backdrop)}
  .flyer{
    position:absolute;left:50px;top:630px;width:1100px;height:1544px;
    background:var(--paper);overflow:hidden;
    font-family:"Roboto",Arial,sans-serif;color:var(--ink);
    box-shadow:0 6px 24px rgba(0,0,0,.12);
  }
  .brand{position:absolute;left:93px;top:100px;display:flex;align-items:center;gap:16px}
  .brand-mark{width:44px;height:44px;background:var(--brand-orange)}
  .brand-name{font-family:"Montserrat",sans-serif;font-weight:800;font-size:44px;color:var(--brand-blue);letter-spacing:.5px}
  .top-stripes{position:absolute;left:0;top:207px;width:1100px;height:76px}
  .hero{position:absolute;left:0;top:283px;width:1100px;height:366px;background:var(--brand-blue)}
  .hero-photo{
    position:absolute;left:500px;top:0;width:600px;height:366px;
    background:linear-gradient(90deg,rgba(18,63,138,1) 0%,rgba(18,63,138,.3) 18%,rgba(0,0,0,0) 30%),
               linear-gradient(180deg,#6f8fb8 0%,#c99a78 42%,#4d5662 62%,#2d333b 100%);
  }
  .headline{position:absolute;left:88px;top:52px;font-family:"Montserrat",sans-serif;font-weight:800;line-height:.92}
  .headline .line-small{display:block;color:#fff;font-size:76px;letter-spacing:-1px}
  .headline .line-big{display:block;color:var(--brand-orange);font-size:108px;letter-spacing:-3px}
  .label{position:absolute;left:90px;top:649px;width:440px;height:80px}
  .label-text{position:absolute;left:26px;top:16px;font-family:"Roboto Condensed",sans-serif;font-weight:700;font-size:37px;color:#fff}
  .body-col{position:absolute;font-size:17.4px;line-height:20.2px;text-align:justify;hyphens:auto}
  .body-col p+p{margin-top:20px}
  .col-left{left:88px;top:778px;width:424px}
  .col-right{left:581px;top:730px;width:439px}
  .road-photo{
    position:absolute;left:581px;top:1138px;width:439px;height:186px;
    background:linear-gradient(160deg,#b9c9b2 0%,#8e9a8a 40%,#6f7476 70%,#5b6266 100%);
  }
  .divider{position:absolute;left:96px;top:1383px;width:924px;height:2px;background:#333}
  .contact{position:absolute;top:1410px}
  .contact-role{font-family:"Montserrat",sans-serif;font-weight:600;font-size:22px;color:var(--ink);margin-left:35px}
  .contact-phone{display:flex;align-items:center;gap:10px;font-family:"Montserrat",sans-serif;font-weight:800;font-size:31px;color:var(--brand-blue);line-height:1}
  .contact-phone svg{width:24px;height:24px}
  .ceo{left:96px}
  .cfo{left:373px}
  .company-info{position:absolute;left:685px;top:1410px;font-family:"Montserrat",sans-serif;font-weight:600;font-size:21px;line-height:32px;color:var(--ink)}
</style>
</head>
<body>
<main class="flyer">
  <header class="brand">
    <span class="brand-mark"></span>
    <span class="brand-name">DWR Logistics LLC</span>
  </header>

  <svg class="top-stripes" viewBox="0 0 1100 76" aria-hidden="true">
    <polygon points="700,0 716,0 676,76 660,76" fill="var(--brand-orange)"/>
    <polygon points="727,0 743,0 703,76 687,76" fill="var(--brand-orange)"/>
    <polygon points="754,0 1100,0 1100,76 714,76" fill="var(--brand-orange)"/>
  </svg>

  <section class="hero">
    <div class="hero-photo" role="img" aria-label="Photo of a white semi-truck with a grey curtain trailer driving on a highway at dusk"></div>
    <h1 class="headline">
      <span class="line-small">LOGISTICS</span>
      <span class="line-big">MADE</span>
      <span class="line-big">SIMPLE</span>
    </h1>
  </section>

  <div class="label">
    <svg width="440" height="80" viewBox="0 0 440 80" aria-hidden="true">
      <polygon points="0,0 372,0 332,80 0,80" fill="var(--brand-orange)"/>
      <polygon points="385,0 400,0 360,80 345,80" fill="var(--brand-orange)"/>
      <polygon points="412,0 427,0 387,80 372,80" fill="var(--brand-orange)"/>
    </svg>
    <span class="label-text">DWR Logistics LLC</span>
  </div>

  <article class="body-col col-left">
    <p>is a transportation company that specializes in maximizing the efficiency in moving products from shipper to customer in the shortest, safest time possible. We have the knowledge and ability to handle any dry van, reefer, flatbed, or tanker load that needs to be moved. We strive to be your number one call to bring or move any product that your company may need. With our current 30 truck fleet, we can service customers locally to across country with solo and team drivers to make sure that your product is to your customers in the time frame promised. DWR can additionally adjust to each customer's needs so If the need arises, we can add to the fleet to make sure that you, the customer, are getting the service that you need.</p>
    <p>We take pride in our work and our customer service from pick up to delivery. Our current customer list handles more than half of the nation's imported orange juice, hauling the corn oil that fries the potatoes chips for the one of the nations largest potato chip suppliers, to hauling wine from the west coast doing plant to plant transfers to the plants on the east coast. We also branch out to haul the corn syrup in to make the wine and alcohol out of the plant in the Midwest to the different plants that make alcohol. In short, from a transportation standpoint if you need it, we can bring it to you rather it is the ingredient's coming into your plant or your product leaving.</p>
  </article>

  <article class="body-col col-right">
    <p>To date, we have won the Keystone Elite Carrier Excellence Award two years in a row servicing their major customers across their different brokerage networks. DWR is the number one truck supplier to two of the major orange juice manufacturers in the US for when they bring their product into port side in Florida, and it needs to go to their manufacturing facility throughout the state. In the past year, we have hauled over 40 million gallons of orange juice, another million gallons of wine and alcohol and millions of gallons of corn oil to service the nation's food industry with the ability to add to that ever-growing number.</p>
    <p>What sets us apart from any other carrier is that when you call you will get either the owner or the CFO, you will not have to wait for approvals and time wasted. We work through the problems to find the right solution then get it executed quickly and effectively. You are not just another number to us you are what makes our company possible, and we value that relationship.</p>
  </article>

  <div class="road-photo" role="img" aria-label="Aerial photo of white trucks driving on a divided highway through green fields"></div>

  <div class="divider"></div>

  <div class="contact ceo">
    <div class="contact-role">CEO Mark Ellison</div>
    <div class="contact-phone">
      <svg viewBox="0 0 24 24" aria-hidden="true"><path d="M6.6 10.8c1.4 2.8 3.8 5.1 6.6 6.6l2.2-2.2c.3-.3.7-.4 1-.2 1.1.4 2.3.6 3.6.6.6 0 1 .4 1 1V20c0 .6-.4 1-1 1C10.6 21 3 13.4 3 4c0-.6.4-1 1-1h3.5c.6 0 1 .4 1 1 0 1.3.2 2.5.6 3.6.1.3 0 .7-.2 1z" fill="var(--brand-orange)"/></svg>
      555-014-2287
    </div>
  </div>
  <div class="contact cfo">
    <div class="contact-role">CFO Paul Renner</div>
    <div class="contact-phone">
      <svg viewBox="0 0 24 24" aria-hidden="true"><path d="M6.6 10.8c1.4 2.8 3.8 5.1 6.6 6.6l2.2-2.2c.3-.3.7-.4 1-.2 1.1.4 2.3.6 3.6.6.6 0 1 .4 1 1V20c0 .6-.4 1-1 1C10.6 21 3 13.4 3 4c0-.6.4-1 1-1h3.5c.6 0 1 .4 1 1 0 1.3.2 2.5.6 3.6.1.3 0 .7-.2 1z" fill="var(--brand-orange)"/></svg>
      555-016-3391
    </div>
  </div>
  <address class="company-info" style="font-style:normal">
    dwrlogisticsllc@example.com<br>
    410 Maple Ct. Fairview, IN. 47000
  </address>
</main>
</body>
</html>
```